ambitious event and festival agency from austria needs fresh business card design

A new design is due for the new headquarters and the new challenges. We organize events for different target groups from 16 to 60 years. The design should therefore be straightforward and not confused, so we are open to new colors and the logo may also be changed. In general, however, the most interesting suggestions are the most interesting ones. after this order we are looking for more graphics for quillvane facebook instagramm homepage etc A new design is due for the new headquarters and the new challenges. We organize events for different target groups from 16 to 60 years. The design should therefore be straightforward and not confused, so we are open to new colors and the logo may also be changed. In general, however, the most interesting suggestions are the most interesting ones. after this order we are looking for more graphics for quillvane facebook instagramm homepage etc A new design is due for the new headquarters and the new challenges. We organize events for different target groups from 16 to 60 years. The design should therefore be straightforward and not confused, so we are open to new colors and the logo may also be changed. In general, however, the most interesting suggestions are the most interesting ones. after this order we are looking for more graphics for quillvane facebook instagramm homepage etc
Updates

Reason: I am sorry for this decision but i need some more time. No new designs please, there are so many good ones and I will have made a decision in the next 3 days.

Target Market(s)

Industry/Entity Type

Business

Font styles to use
Serif
Sans Serif

Colors

Designer to choose colors to be used in the design.

Requirements
Must have
Nice to have
Should not have

```html
<!DOCTYPE html>
<html lang="en">
<head>
<meta charset="utf-8">
<title>quillvane – business card</title>
<link rel="stylesheet" href="https://fonts.googleapis.com/css2?family=Oswald:wght@600&family=Work+Sans:wght@300;500&display=swap">
<style>
  :root {
    --backdrop: #1f1f21;
    --card-white: #ffffff;
    --card-black: #0b0b0c;
    --card-black-soft: #2a2a2c;
    --brand-red: #a3273b;
    --ink-grey: #7a7a7a;
    --logo-grey: #6e6e6e;
  }
  * { box-sizing: border-box; margin: 0; padding: 0; }
  html, body {
    width: 1200px; height: 900px; overflow: hidden;
    background: var(--backdrop);
  }
  .canvas {
    width: 1200px; height: 900px;
    display: flex; flex-direction: column; align-items: center; justify-content: center;
    gap: 40px;
  }
  .card {
    width: 700px; height: 400px;
    border-radius: 26px;
    position: relative;
    overflow: hidden;
    box-shadow: 0 16px 40px rgba(0,0,0,.5);
  }
  .card--front { background: var(--card-white); }
  .card--back {
    background: linear-gradient(120deg, var(--card-black-soft) 0%, var(--card-black) 55%, #000 100%);
    display: flex; align-items: center; justify-content: center;
  }

  .wordmark {
    display: flex; align-items: center; gap: 12px;
    font-family: "Work Sans", sans-serif; font-weight: 500;
    color: var(--logo-grey);
    letter-spacing: -0.5px; line-height: 1;
  }
  .wordmark__square { background: var(--brand-red); flex: none; }
  .card--front .wordmark { position: absolute; left: 40px; top: 34px; font-size: 54px; }
  .card--front .wordmark__square { width: 16px; height: 16px; }
  .card--back .wordmark { font-size: 84px; color: #8a8a8a; gap: 18px; }
  .card--back .wordmark__square { width: 22px; height: 22px; }

  .contact {
    position: absolute; left: 44px; top: 168px;
    font-family: "Work Sans", sans-serif; font-weight: 300;
    color: var(--ink-grey); font-size: 17px; line-height: 1.35;
  }
  .contact__name {
    font-family: "Oswald", sans-serif; font-weight: 600;
    color: var(--brand-red); font-size: 27px; line-height: 1.1;
    text-transform: uppercase; letter-spacing: 0.3px;
  }
  .contact__role { margin-bottom: 12px; }
  .contact__address { margin-bottom: 10px; }
  .contact__line { display: flex; align-items: center; gap: 12px; }
  .contact__icon { width: 14px; height: 14px; flex: none; }
  .contact__accent { color: var(--brand-red); }
</style>
</head>
<body>
<main class="canvas">
  <section class="card card--front">
    <div class="wordmark"><span class="wordmark__square"></span>quillvane</div>
    <div class="contact">
      <p class="contact__name">Marlen Hofbauer</p>
      <p class="contact__role">Manager</p>
      <p class="contact__address">quillvane<br>Lindenweg 12<br>A4820 Traunfeld</p>
      <p class="contact__line">
        <svg class="contact__icon" viewBox="0 0 14 14" fill="none" stroke="#a3273b" stroke-width="1.3"><rect x="4" y="1" width="6" height="12" rx="1.2"/><line x1="6" y1="11" x2="8" y2="11"/></svg>
        + 43 660 418 273 5
      </p>
      <p class="contact__line">
        <svg class="contact__icon" viewBox="0 0 14 14" fill="none" stroke="#a3273b" stroke-width="1.3"><rect x="1" y="3" width="12" height="8" rx="1"/><polyline points="1,3 7,8 13,3"/></svg>
        m.hofbauer@quillvane.eu
      </p>
      <p class="contact__line">
        <svg class="contact__icon" viewBox="0 0 14 14" fill="none" stroke="#a3273b" stroke-width="1.2"><circle cx="7" cy="7" r="6"/><ellipse cx="7" cy="7" rx="2.6" ry="6"/><line x1="1" y1="7" x2="13" y2="7"/></svg>
        <span>www.<span class="contact__accent">quillvane</span>.eu</span>
      </p>
    </div>
  </section>

  <section class="card card--back">
    <div class="wordmark"><span class="wordmark__square"></span>quillvane</div>
  </section>
</main>
</body>
</html>
```